NZ First of it's kind solutions directory and marketplace for busy Mums needs a business card design

We need a business card design for our new nationwide business in NZ (long term plans to go global). We provide solutions to the everyday challenges that busy Mums face by connecting them with quality communities and suppliers of carefully selected, relevant products and services. We sell direct via our online marketplace. The final design should communicate our values of inclusivity, quality and smart solutions. Colours should incorporate our logo colour palette of #477077 and #6ba8b2. Our website is at https://www.brightnestly.com

Target Market(s)

busy Mums, Age 28 – 50, female, income over $100K, location main centres NZ primarily but NZ wide. Is likely juggling work or career with a young family. Probably had hobbies which have fallen by the wayside.
-Wants to succeed in her chosen career without compromising on family life
-to successfully juggle her career without feeling like she is compromising her children
- Is time poor, something always has to give and it’s generally her health (she’ll stay up late, get stressed)
- probably ex corporate or professional career. Has discretional income

Industry/Entity Type

Business

Contact Information for Business Card

Lena Hartwell, Founder, BrightNestly.com (Strapline Click; Connect; Done), 48 Kowhai Terrace, Ferndale, Auckland 1071, New Zealand. Mob: 021 437 518 Ph: +64 (0)9 581 4706

Font styles to use
Other font styles liked:
• Raleway, and/or Architects Daughter

Colors
00a990
33b8a4
86cfc6
cfeae6

Requirements
Must have
• the above details, streamline. the logo and colours associated with those logos
Should not have
• foil or metallic colours

```html
<!DOCTYPE html>
<html lang="en">
<head>
<meta charset="utf-8">
<title>BrightNestly – Business Card</title>
<link rel="stylesheet" href="https://fonts.googleapis.com/css2?family=Varela+Round&family=Roboto:ital,wght@0,400;1,400&display=swap">
<style>
  :root {
    --brand-dark: #477077;
    --brand-light: #6ba8b2;
    --ink: #3b3f42;
    --muted: #4a4e52;
    --card: #ffffff;
    --backdrop: #e6e6e6;
    --card-edge: #d6d6d6;
  }
  * { margin: 0; padding: 0; box-sizing: border-box; }
  html, body {
    width: 1200px;
    height: 576px;
    overflow: hidden;
    background: var(--backdrop);
  }
  .canvas {
    position: relative;
    width: 1200px;
    height: 576px;
  }
  .card {
    position: absolute;
    top: 138px;
    width: 484px;
    height: 292px;
    background: var(--card);
    border: 1px solid var(--card-edge);
    border-radius: 14px;
  }
  .card--front { left: 82px; }
  .card--back { left: 602px; }

  /* Front */
  .brand-dot {
    position: absolute;
    left: 50%;
    top: 62px;
    width: 56px;
    height: 56px;
    margin-left: -28px;
    border-radius: 50%;
    background: var(--brand-dark);
  }
  .brand-name {
    position: absolute;
    left: 0;
    right: 0;
    top: 164px;
    text-align: center;
    font-family: "Varela Round", sans-serif;
    font-size: 33px;
    line-height: 1;
    color: var(--brand-dark);
    letter-spacing: -0.5px;
  }
  .strapline {
    position: absolute;
    left: 0;
    right: 0;
    top: 207px;
    text-align: center;
    font-family: "Roboto", sans-serif;
    font-size: 12px;
    line-height: 16px;
    color: var(--muted);
  }

  /* Back */
  .identity {
    position: absolute;
    right: 260px;
    top: 111px;
    text-align: right;
    font-family: "Roboto", sans-serif;
    color: var(--muted);
  }
  .identity__name {
    font-family: "Varela Round", sans-serif;
    font-size: 19px;
    line-height: 22px;
    color: var(--brand-dark);
    font-weight: 400;
  }
  .identity__role {
    font-style: italic;
    font-size: 12px;
    line-height: 16px;
    margin-bottom: 6px;
  }
  .identity__address {
    font-style: normal;
    font-size: 12px;
    line-height: 19px;
  }
  .contact-list {
    position: absolute;
    left: 246px;
    top: 113px;
    list-style: none;
    font-family: "Roboto", sans-serif;
    font-size: 12px;
    line-height: 18.5px;
    color: var(--muted);
  }
  .contact-list li {
    display: flex;
    align-items: center;
    gap: 8px;
  }
  .contact-list svg {
    width: 11px;
    height: 11px;
    flex: none;
    fill: var(--brand-dark);
  }
</style>
</head>
<body>
<main class="canvas">
  <section class="card card--front" aria-label="Card front">
    <div class="brand-dot"></div>
    <div class="brand-name">BrightNestly</div>
    <p class="strapline">Smart solutions for busy mums</p>
  </section>

  <section class="card card--back" aria-label="Card back">
    <div class="identity">
      <h1 class="identity__name">Lena Hartwell</h1>
      <p class="identity__role">Founder</p>
      <address class="identity__address">48 Kowhai Terrace, Ferndale,<br>Auckland 1071, New Zealand</address>
    </div>
    <ul class="contact-list">
      <li>
        <svg viewBox="0 0 12 12" aria-hidden="true"><rect x="3" y="0.5" width="6" height="11" rx="1.2"/><rect x="4" y="2" width="4" height="6.5" fill="#fff"/></svg>
        021 437 518
      </li>
      <li>
        <svg viewBox="0 0 12 12" aria-hidden="true"><path d="M1 4.5C1 2.5 3 1.5 6 1.5s5 1 5 3v1H8.5V4.3H3.5v1.2H1z"/><path d="M2.5 11l1-4.5h5l1 4.5z"/></svg>
        +64 (0)9 581 4706
      </li>
      <li>
        <svg viewBox="0 0 12 12" aria-hidden="true"><rect x="0.5" y="2" width="11" height="8"/><path d="M0.8 2.4L6 6.6l5.2-4.2" stroke="#fff" stroke-width="1" fill="none"/></svg>
        www.BrightNestly.com
      </li>
      <li>
        <svg viewBox="0 0 12 12" aria-hidden="true"><circle cx="6" cy="6" r="5.2" fill="none" stroke="#477077" stroke-width="1.2"/><ellipse cx="6" cy="6" rx="2.2" ry="5.2" fill="none" stroke="#477077" stroke-width="1"/><path d="M1 6h10" stroke="#477077" stroke-width="1"/></svg>
        lenahartwell@brightnestly.com
      </li>
    </ul>
  </section>
</main>
</body>
</html>
```